Wine Bottle Label Logo Design

My fiancé and I are getting married in September and we made homemade wine which will be given to the guests as a wedding favor. We need label/logo for our wine bottles. We were looking for something rustic yet modern and simple. We had an idea for beige and cranberry colored wine stained, weathered, imperfect heart. Things that will need to be incorporated into the label design are as follows:
Our last name and also the name of the wine: Fusaldi
The year: 2012
Where is says Alcohol Content on a wine bottle normally write: Alcohol: Deceiving% by vol.
Type of wine: Red Wine
Incorporate our wedding date: Foot Stomped and Bottled for Nadia and Gus's Wedding Day 9/28/13
Wedding

```html
<!DOCTYPE html>
<html lang="en">
<head>
<meta charset="utf-8">
<title>Fusaldi 2012 – Wine Label</title>
<link rel="stylesheet" href="https://fonts.googleapis.com/css2?family=Josefin+Sans:wght@300;400&display=swap">
<style>
  :root {
    --ink-black: #000000;
    --frame-red: #9c1d20;
    --panel-red: #8b2528;
    --panel-shade: #7d2024;
    --label-white: #ffffff;
    --text-shadow: #000000;
    --art-beige: #c9a06a;
    --art-dark: #5a3a30;
  }
  html, body {
    margin: 0;
    padding: 0;
    width: 1200px;
    height: 1050px;
    overflow: hidden;
    background: var(--ink-black);
  }
  .label {
    position: relative;
    width: 1200px;
    height: 1050px;
    background: var(--ink-black);
    font-family: "Josefin Sans", "Century Gothic", sans-serif;
    font-weight: 300;
    color: var(--label-white);
  }
  .label__frame {
    position: absolute;
    left: 18px; top: 18px; right: 18px; bottom: 18px;
    background: var(--frame-red);
  }
  .label__panel {
    position: absolute;
    left: 52px; top: 48px; right: 52px; bottom: 46px;
    background: radial-gradient(ellipse at 50% 55%, var(--panel-red) 0%, var(--panel-red) 55%, var(--panel-shade) 100%);
  }
  .label__vineyard {
    position: absolute;
    inset: 0;
    background: linear-gradient(180deg, rgba(140,40,44,0) 0%, rgba(120,30,34,0.35) 60%, rgba(110,28,32,0.5) 100%);
  }
  .text-line {
    position: absolute;
    left: 0; right: 0;
    text-align: center;
    margin: 0;
    white-space: nowrap;
    text-shadow: 3px 3px 0 var(--text-shadow);
    line-height: 1;
    font-weight: 300;
  }
  .condensed {
    transform: scaleX(0.8);
    transform-origin: 600px 0;
  }
  .wine-name {
    top: 60px;
    font-size: 170px;
    letter-spacing: -6px;
    transform: scaleX(0.86);
    transform-origin: 600px 0;
  }
  .vintage {
    top: 214px;
    font-size: 56px;
    padding-left: 60px;
  }
  .barrel-art {
    position: absolute;
    left: 420px;
    top: 300px;
    width: 345px;
    height: 272px;
    background: linear-gradient(160deg, var(--art-beige) 0%, var(--art-beige) 45%, var(--art-dark) 100%);
    opacity: 0.55;
  }
  .dedication {
    top: 600px;
    font-size: 46px;
  }
  .couple {
    top: 662px;
    font-size: 112px;
    letter-spacing: -3px;
    transform: scaleX(0.84);
    transform-origin: 600px 0;
  }
  .wedding-date {
    top: 772px;
    font-size: 54px;
  }
  .tasting-note {
    top: 850px;
    font-size: 42px;
    line-height: 50px;
  }
  .alcohol {
    top: 958px;
    left: auto;
    right: 64px;
    text-align: right;
    font-size: 36px;
    text-shadow: 2px 2px 0 var(--text-shadow);
    transform: scaleX(0.8);
    transform-origin: 100% 0;
  }
</style>
</head>
<body>
  <main class="label">
    <div class="label__frame"></div>
    <div class="label__panel">
      <div class="label__vineyard" role="img" aria-label="Faint photograph of a vineyard with barrels, tinted red"></div>
    </div>

    <h1 class="text-line wine-name">Fusaldi</h1>
    <p class="text-line vintage condensed">2012</p>

    <div class="barrel-art" role="img" aria-label="Illustration of a wooden wine barrel on its side with a cluster of dark grapes and vine leaves"></div>

    <p class="text-line dedication condensed">Foot Stomped and Bottled for</p>
    <h2 class="text-line couple">Nadia &amp; Gus</h2>
    <p class="text-line wedding-date condensed">9/28/13</p>
    <p class="text-line tasting-note condensed">Aged outdoors during the cold winter months to allow for a slower<br>fermentation process. Its like a warm sweet hug in a bottle.</p>
    <p class="text-line alcohol">Deceiving% Alc/Vol</p>
  </main>
</body>
</html>
```